a business advisory consulting website

I need a website 3-5 pages to sell my professional services in IT and Project management Consulting. My company name is Tidewell Advisory Consulting. I want it to be device friendly and easy to navigate for the busy executive however intriguing enough.
I have attached some info I drafted on About the company and personal Bio. Also there is a website that I really like that I have attached the initial site pdf and websites that I like are here: https://quillmarkfunds.example, https://lumetratrends.example, https://www.corbelteachingconsulting.example as examples. Thanks
Updates

Hi Designers, I have uploaded the logo in 3D .png format, to assist in the web design.

Target Market(s)

B2B, governments, IT companies, Project Management companies and Consulting firms, small medium enterprises to large corporate enterprises.

Industry/Entity Type

It Professional

Coding

Coded - Design and coding required

Number of Pages Required

5+ page

Font styles to use
Sans Serif

Requirements
Must have
• Home, About company, the team, what we do and contact us
Nice to have
• Blog
Should not have
• pop ups, flash

```html
<!DOCTYPE html>
<html lang="en">
<head>
<meta charset="utf-8">
<title>Tidewell Advisory Consulting</title>
<link href="https://fonts.googleapis.com/css2?family=Poppins:wght@300;400;500;600;700&family=Rajdhani:wght@700&display=swap" rel="stylesheet">
<style>
:root{
  --red:#d7282f;
  --navy:#1f2640;
  --pink:#fdf1f0;
  --ink:#2a2d3a;
  --grey:#7d7f88;
  --line:#e7e7ea;
  --white:#ffffff;
}
*{box-sizing:border-box;margin:0;padding:0}
html,body{width:1200px;height:5146px;overflow:hidden}
body{position:relative;background:var(--white);font-family:'Poppins',sans-serif;color:var(--ink)}
.abs{position:absolute}
.pink{background:var(--pink);position:absolute}
.dots{position:absolute;background-image:radial-gradient(var(--red) 1.2px,transparent 1.4px);background-size:9px 9px;opacity:.55}
.photo{position:absolute}
.red{color:var(--red)}

/* header */
.brand{position:absolute;display:flex;align-items:center;gap:10px}
.brand-mark{width:26px;height:26px;background:var(--red)}
.brand-name{font-family:'Poppins',sans-serif;font-weight:700;color:var(--navy);font-size:17px;line-height:17px;letter-spacing:.5px}
.nav{position:absolute;top:30px;left:600px;display:flex;gap:28px;font-size:10.5px;text-transform:uppercase;color:var(--grey);align-items:center}
.nav a{color:inherit;text-decoration:none}
.nav a.active{color:var(--red)}

/* hero */
.hero-title{position:absolute;left:162px;top:186px;font-family:'Rajdhani',sans-serif;font-weight:700;font-size:52px;line-height:53px;color:var(--navy);letter-spacing:.5px}
.text{font-size:12px;line-height:21px;color:var(--grey)}
.text-sm{font-size:10.5px;line-height:18px;color:var(--grey)}

.btn{position:absolute;height:44px;border-radius:22px;background:var(--red);color:var(--white);font-size:11.5px;font-weight:500;text-transform:uppercase;display:flex;align-items:center;padding-left:18px;box-shadow:0 4px 0 rgba(215,40,47,.25)}
.btn .go{position:absolute;right:4px;top:4px;width:36px;height:36px;border-radius:50%;background:var(--white);border:2px solid var(--red);display:flex;align-items:center;justify-content:center}

.h2{position:absolute;font-size:32px;font-weight:300;color:var(--navy);text-transform:uppercase;line-height:38px}
.h2 b{font-weight:600;color:var(--red)}

/* services */
.svc-icon{position:absolute;width:76px;height:76px;border-radius:50%;background:var(--navy)}
.svc-icon .badge{position:absolute;right:-14px;bottom:-6px;width:30px;height:30px;border-radius:50%;background:var(--white);border:2px solid var(--red);display:flex;align-items:center;justify-content:center}
.svc-title{position:absolute;font-size:22px;font-weight:500;color:var(--red);line-height:28px}
.bullets{position:absolute;list-style:none;font-size:11px;line-height:19px;color:var(--grey)}
.bullets li{position:relative;padding-left:30px;margin-bottom:11px}
.bullets li svg{position:absolute;left:0;top:3px}

/* contact */
.field{position:absolute;left:162px;width:464px;border:1px solid var(--line);font-size:10.5px;color:var(--grey);padding:14px 16px;background:var(--white)}
.field i{color:var(--red);font-style:normal}
.info-card{position:absolute;left:760px;top:3192px;width:280px;height:256px;background:var(--white);box-shadow:0 0 18px rgba(0,0,0,.07);padding:30px 18px}
.info-card h4{font-size:14px;font-weight:400;color:var(--red);margin-bottom:6px}
.info-card p{margin-bottom:20px}

/* blog */
.meta{font-size:10.5px;color:var(--red)}
.post-title{font-size:15px;font-weight:500;line-height:22px;color:var(--navy)}

/* footer */
.foot-links{position:absolute;top:4954px;left:0;width:1200px;display:flex;justify-content:center;gap:22px;font-size:10.5px;color:var(--grey)}
.social{position:absolute;width:34px;height:34px;border-radius:50%;background:#2f86c8}
.copy{position:absolute;top:5100px;width:1200px;text-align:center;font-size:9px;color:var(--red)}
</style>
</head>
<body>

<!-- ============ HEADER / HERO ============ -->
<div class="pink" style="left:676px;top:0;width:524px;height:676px"></div>

<div class="brand" style="left:162px;top:32px">
  <span class="brand-mark"></span>
  <span class="brand-name">TIDEWELL<br>ADVISORY</span>
</div>

<nav class="nav">
  <a class="active" href="#">Home</a>
  <a href="#">About Us</a>
  <a href="#">The Team</a>
  <a href="#">What We Do</a>
  <a href="#">Contact Us</a>
  <svg width="16" height="16" viewBox="0 0 16 16"><circle cx="7" cy="7" r="5" fill="none" stroke="#d7282f" stroke-width="1.6"/><line x1="10.5" y1="10.5" x2="14.5" y2="14.5" stroke="#d7282f" stroke-width="1.6"/></svg>
</nav>

<div class="dots" style="left:552px;top:536px;width:184px;height:96px"></div>
<div class="photo" role="img" aria-label="Photo of consultants shaking hands across a meeting table" style="left:600px;top:76px;width:526px;height:524px;background:linear-gradient(135deg,#c9c6c2,#8d8a88 45%,#b3b0ad 70%,#e3e1de)"></div>

<h1 class="hero-title"><span class="red">IT AND PROJECT</span><br>MANAGEMENT<br><span class="red">CONSULTING</span></h1>
<p class="abs text" style="left:162px;top:356px;width:370px">Lorem ipsum dolor sit amet, consectetur adipiscing elit, sed do eiusmod tempor incididunt ut labore et dolore magna aliqua. Ut enim ad minim veniam.</p>
<div class="btn" style="left:162px;top:442px;width:156px">Contact Us<span class="go"><svg width="14" height="14" viewBox="0 0 14 14"><path d="M3 11 L11 3 M5 3 H11 V9" stroke="#d7282f" stroke-width="2" fill="none"/></svg></span></div>

<!-- ============ ABOUT ============ -->
<div class="pink" style="left:162px;top:780px;width:374px;height:330px"></div>
<div class="dots" style="left:390px;top:1050px;width:182px;height:96px"></div>
<div class="photo" role="img" aria-label="Photo of a smiling businessman in glasses holding a laptop" style="left:250px;top:736px;width:320px;height:374px;background:linear-gradient(180deg,#e9eef5,#c5d3e6 40%,#4b5266 75%,#2c2f38);border-radius:4px"></div>

<h2 class="h2" style="left:662px;top:732px">About <b>Company</b></h2>
<p class="abs" style="left:662px;top:784px;width:380px;font-size:12.5px;line-height:21px;color:#555">Lorem ipsum dolor sit amet, consectetur adipiscing elit, sed do eiusmod tempor incididunt ut labore.</p>
<p class="abs text-sm" style="left:662px;top:840px;width:380px">Lorem ipsum dolor sit amet, consectetur adipiscing elit, sed eiusmod tempor incididunt ut labore et dolore magna aliqua. Ut enim ad minim veniam, quis nostrud exercitation ullamco laboris nisi ut aliquip ex ea commodo consequat. Duis aute irure dolor in reprehenderit in there its voluptate velit esse cillum dolore eu fugiat nulla pariatur. Excepteur sint occaecat cupidatat non proident, sunt in culpa qui officia deserunt mollit anim id est laborum.</p>
<p class="abs text-sm" style="left:662px;top:984px;width:380px">Lorem ipsum dolor sit amet, consectetur adipiscing elit, sed eiusmod tempor incididunt ut labore et dolore magna aliqua. Ut enim ad minim veniam, quis nostrud exercitation ullamco laboris nisi ut aliquip.</p>
<div class="btn" style="left:662px;top:1066px;width:156px">Learn More<span class="go"><svg width="14" height="14" viewBox="0 0 14 14"><path d="M3 11 L11 3 M5 3 H11 V9" stroke="#d7282f" stroke-width="2" fill="none"/></svg></span></div>

<!-- ============ WHAT WE DO ============ -->
<h2 class="h2" style="left:0;width:1200px;text-align:center;top:1204px">What <b>We Do</b></h2>

<!-- service 1 -->
<div class="pink" style="left:916px;top:1278px;width:284px;height:374px"></div>
<div class="dots" style="left:614px;top:1560px;width:92px;height:92px"></div>
<div class="photo" role="img" aria-label="Photo of a man celebrating at his laptop on a desk" style="left:650px;top:1334px;width:390px;height:260px;background:linear-gradient(135deg,#e8ebef,#c9ced6 50%,#6f6a63)"></div>
<div class="svc-icon" style="left:162px;top:1274px"><svg width="76" height="76" viewBox="0 0 76 76"><circle cx="28" cy="30" r="4" fill="none" stroke="#fff" stroke-width="1.6"/><path d="M32 30 Q44 22 50 34" fill="none" stroke="#fff" stroke-width="1.6" stroke-dasharray="3 2"/><path d="M24 46 L30 52 M30 46 L24 52 M44 44 L50 50 M50 44 L44 50" stroke="#fff" stroke-width="1.6"/></svg><span class="badge"><svg width="12" height="12" viewBox="0 0 14 14"><path d="M3 11 L11 3 M5 3 H11 V9" stroke="#d7282f" stroke-width="2" fill="none"/></svg></span></div>
<h3 class="svc-title" style="left:162px;top:1370px">Market Entry</h3>
<ul class="bullets" style="left:162px;top:1418px;width:380px">
  <li><svg width="14" height="12" viewBox="0 0 14 12"><path d="M1 1 L7 7 L13 1 L13 5 L7 11 L1 5Z" fill="#d7282f"/></svg>Lorem ipsum dolor sit amet, consectetur adipiscing elit, sed deiusmod tempor incididunt ut labore.</li>
  <li><svg width="14" height="12" viewBox="0 0 14 12"><path d="M1 1 L7 7 L13 1 L13 5 L7 11 L1 5Z" fill="#d7282f"/></svg>Lorem ipsum dolor sit amet, consectetur adipiscing elit.</li>
  <li><svg width="14" height="12" viewBox="0 0 14 12"><path d="M1 1 L7 7 L13 1 L13 5 L7 11 L1 5Z" fill="#d7282f"/></svg>Lorem ipsum dolor consectetur adipiscing elit.</li>
  <li><svg width="14" height="12" viewBox="0 0 14 12"><path d="M1 1 L7 7 L13 1 L13 5 L7 11 L1 5Z" fill="#d7282f"/></svg>Lorem ipsum dolor consectetur adipiscing elit.</li>
  <li><svg width="14" height="12" viewBox="0 0 14 12"><path d="M1 1 L7 7 L13 1 L13 5 L7 11 L1 5Z" fill="#d7282f"/></svg>Lorem ipsum dolor sit amet, consectetur adipiscing elit, sed deiusmod tempor incididunt ut labore.</li>
</ul>

<!-- service 2 -->
<div class="pink" style="left:0;top:1712px;width:286px;height:376px"></div>
<div class="dots" style="left:494px;top:1990px;width:94px;height:98px"></div>
<div class="photo" role="img" aria-label="Photo of a doctor working with a holographic medical interface" style="left:162px;top:1768px;width:390px;height:262px;background:linear-gradient(135deg,#2c6a80,#6fb3c4 45%,#1f4f63)"></div>
<div class="svc-icon" style="left:668px;top:1714px"><svg width="76" height="76" viewBox="0 0 76 76"><rect x="24" y="24" width="24" height="22" fill="none" stroke="#fff" stroke-width="1.6"/><path d="M28 40 L34 34 L38 38 L44 30" fill="none" stroke="#fff" stroke-width="1.6"/><path d="M30 50 H42" stroke="#fff" stroke-width="1.6"/></svg><span class="badge"><svg width="12" height="12" viewBox="0 0 14 14"><path d="M3 11 L11 3 M5 3 H11 V9" stroke="#d7282f" stroke-width="2" fill="none"/></svg></span></div>
<h3 class="svc-title" style="left:668px;top:1806px;width:380px">Technology Ananlysis within healthcare</h3>
<ul class="bullets" style="left:668px;top:1882px;width:380px">
  <li><svg width="14" height="12" viewBox="0 0 14 12"><path d="M1 1 L7 7 L13 1 L13 5 L7 11 L1 5Z" fill="#d7282f"/></svg>Lorem ipsum dolor sit amet, consectetur adipiscing elit.</li>
  <li><svg width="14" height="12" viewBox="0 0 14 12"><path d="M1 1 L7 7 L13 1 L13 5 L7 11 L1 5Z" fill="#d7282f"/></svg>Lorem ipsum dolor sit amet, consectetur adipiscing elit.</li>
  <li><svg width="14" height="12" viewBox="0 0 14 12"><path d="M1 1 L7 7 L13 1 L13 5 L7 11 L1 5Z" fill="#d7282f"/></svg>Lorem ipsum dolor consectetur adipiscing elit.</li>
  <li><svg width="14" height="12" viewBox="0 0 14 12"><path d="M1 1 L7 7 L13 1 L13 5 L7 11 L1 5Z" fill="#d7282f"/></svg>Lorem ipsum dolor consectetur adipiscing elit.</li>
  <li><svg width="14" height="12" viewBox="0 0 14 12"><path d="M1 1 L7 7 L13 1 L13 5 L7 11 L1 5Z" fill="#d7282f"/></svg>Lorem ipsum dolor sit amet, consectetur.</li>
</ul>

<!-- service 3 -->
<div class="pink" style="left:916px;top:2148px;width:284px;height:376px"></div>
<div class="dots" style="left:614px;top:2430px;width:92px;height:94px"></div>
<div class="photo" role="img" aria-label="Photo of two business people talking in armchairs, seen from above" style="left:650px;top:2204px;width:390px;height:262px;background:radial-gradient(circle at 55% 50%,#4a4d52,#8a8c86 55%,#a7a79e)"></div>
<div class="svc-icon" style="left:162px;top:2150px"><svg width="76" height="76" viewBox="0 0 76 76"><path d="M24 36 Q38 20 52 36 Z" fill="none" stroke="#fff" stroke-width="1.6"/><path d="M38 36 V50 Q38 54 34 52" fill="none" stroke="#fff" stroke-width="1.6"/></svg><span class="badge"><svg width="12" height="12" viewBox="0 0 14 14"><path d="M3 11 L11 3 M5 3 H11 V9" stroke="#d7282f" stroke-width="2" fill="none"/></svg></span></div>
<h3 class="svc-title" style="left:162px;top:2242px;width:380px">Process Improvement with in government</h3>
<ul class="bullets" style="left:162px;top:2318px;width:380px">
  <li><svg width="14" height="12" viewBox="0 0 14 12"><path d="M1 1 L7 7 L13 1 L13 5 L7 11 L1 5Z" fill="#d7282f"/></svg>Lorem ipsum dolor sit amet, consectetur adipiscing elit.</li>
  <li><svg width="14" height="12" viewBox="0 0 14 12"><path d="M1 1 L7 7 L13 1 L13 5 L7 11 L1 5Z" fill="#d7282f"/></svg>Lorem ipsum dolor sit amet, consectetur adipiscing elit.</li>
  <li><svg width="14" height="12" viewBox="0 0 14 12"><path d="M1 1 L7 7 L13 1 L13 5 L7 11 L1 5Z" fill="#d7282f"/></svg>Lorem ipsum dolor consectetur adipiscing elit.</li>
  <li><svg width="14" height="12" viewBox="0 0 14 12"><path d="M1 1 L7 7 L13 1 L13 5 L7 11 L1 5Z" fill="#d7282f"/></svg>Lorem ipsum dolor consectetur adipiscing elit.</li>
  <li><svg width="14" height="12" viewBox="0 0 14 12"><path d="M1 1 L7 7 L13 1 L13 5 L7 11 L1 5Z" fill="#d7282f"/></svg>Lorem ipsum dolor sit amet, consectetur.</li>
</ul>

<!-- service 4 -->
<div class="pink" style="left:0;top:2584px;width:286px;height:374px"></div>
<div class="dots" style="left:494px;top:2860px;width:94px;height:98px"></div>
<div class="photo" role="img" aria-label="Photo of two businessmen reviewing work on a laptop" style="left:162px;top:2640px;width:390px;height:262px;background:linear-gradient(135deg,#3a4256,#8b93a3 45%,#d9dce2)"></div>
<div class="svc-icon" style="left:668px;top:2586px"><svg width="76" height="76" viewBox="0 0 76 76"><rect x="24" y="26" width="28" height="18" fill="none" stroke="#fff" stroke-width="1.6"/><path d="M20 48 H56" stroke="#fff" stroke-width="1.6"/><circle cx="38" cy="34" r="3" fill="none" stroke="#fff" stroke-width="1.6"/></svg><span class="badge"><svg width="12" height="12" viewBox="0 0 14 14"><path d="M3 11 L11 3 M5 3 H11 V9" stroke="#d7282f" stroke-width="2" fill="none"/></svg></span></div>
<h3 class="svc-title" style="left:668px;top:2678px;width:400px">Advise for early stage startup</h3>
<ul class="bullets" style="left:668px;top:2722px;width:380px">
  <li><svg width="14" height="12" viewBox="0 0 14 12"><path d="M1 1 L7 7 L13 1 L13 5 L7 11 L1 5Z" fill="#d7282f"/></svg>Lorem ipsum dolor sit amet, consectetur adipiscing elit, sed deiusmod tempor incididunt ut labore.</li>
  <li><svg width="14" height="12" viewBox="0 0 14 12"><path d="M1 1 L7 7 L13 1 L13 5 L7 11 L1 5Z" fill="#d7282f"/></svg>Lorem ipsum dolor sit amet, consectetur adipiscing elit.</li>
  <li><svg width="14" height="12" viewBox="0 0 14 12"><path d="M1 1 L7 7 L13 1 L13 5 L7 11 L1 5Z" fill="#d7282f"/></svg>Lorem ipsum dolor consectetur adipiscing elit.</li>
  <li><svg width="14" height="12" viewBox="0 0 14 12"><path d="M1 1 L7 7 L13 1 L13 5 L7 11 L1 5Z" fill="#d7282f"/></svg>Lorem ipsum dolor consectetur adipiscing elit.</li>
  <li><svg width="14" height="12" viewBox="0 0 14 12"><path d="M1 1 L7 7 L13 1 L13 5 L7 11 L1 5Z" fill="#d7282f"/></svg>Lorem ipsum dolor sit amet, consectetur adipiscing elit, sed deiusmod tempor incididunt ut labore.</li>
</ul>

<!-- ============ CONTACT ============ -->
<h2 class="h2" style="left:162px;top:3016px">Speack with <b>Team<br>Member</b></h2>
<p class="abs text" style="left:162px;top:3100px;width:470px">Lorem ipsum dolor sit amet, consectetur adipiscing elieiusmod tempor incididunt ut labore et dolore magna aliqua. Ut enim ad minn veniam, quis nostrud exercitation ullamco laboris.</p>

<div class="field" style="top:3196px;height:40px">First Name <i>*</i></div>
<div class="field" style="top:3256px;height:40px">Email <i>*</i></div>
<div class="field" style="top:3316px;height:40px">Phone <i>*</i></div>
<div class="field" style="top:3370px;height:76px">Message / comments :</div>
<div class="btn" style="left:162px;top:3462px;width:180px">Send Message<span class="go"><svg width="14" height="14" viewBox="0 0 14 14"><path d="M3 11 L11 3 M5 3 H11 V9" stroke="#d7282f" stroke-width="2" fill="none"/></svg></span></div>

<div class="pink" style="left:1000px;top:3150px;width:200px;height:350px"></div>
<div class="dots" style="left:876px;top:3102px;width:184px;height:84px"></div>
<div class="info-card">
  <h4>Office Address</h4>
  <p class="text-sm" style="font-size:10px;line-height:17px">123,Address, State Name, Street Name,<br>City Name, City Name, Zipcode</p>
  <h4>Call for help</h4>
  <p style="font-size:13px;color:#333">(123) 456 - 7890</p>
  <h4>Call for help</h4>
  <p style="font-size:13px;color:#333">info@tidewelladvisory.example</p>
</div>

<!-- ============ BLOG ============ -->
<h2 class="h2" style="left:162px;top:3572px">Latest <b>Blog</b></h2>

<div class="photo" role="img" aria-label="Photo of a team shaking hands around an office table" style="left:162px;top:3640px;width:390px;height:266px;background:linear-gradient(135deg,#b7a79a,#dcd6cf 45%,#6a6f7a)"></div>
<p class="abs meta" style="left:162px;top:3922px">By : Admin &nbsp;&nbsp;|&nbsp;&nbsp; Aug 12,2020</p>
<h3 class="abs post-title" style="left:162px;top:3952px;width:390px">Lorem ipsum dolor sit amet, consect adipiscing elit, sed do eiusmod tempor incididunt.</h3>
<p class="abs text-sm" style="left:162px;top:4004px;width:390px">Lorem ipsum dolor sit amet, consectetur adipiscing elit, sed do eiusmod tempor incididunt ut labore et dolore magna aliqua. Ut enim ad minim commodo consequat.</p>
<p class="abs meta" style="left:162px;top:4078px;font-weight:500">LEARN MORE &nbsp;<svg width="10" height="10" viewBox="0 0 14 14"><path d="M3 11 L11 3 M5 3 H11 V9" stroke="#d7282f" stroke-width="2" fill="none"/></svg></p>

<div class="photo" role="img" aria-label="Photo of colleagues working at a whiteboard" style="left:596px;top:3640px;width:204px;height:136px;background:linear-gradient(135deg,#dfe3e6,#9aa6ae 60%,#5b6470)"></div>
<p class="abs meta" style="left:822px;top:3640px">By : Admin &nbsp;&nbsp;|&nbsp;&nbsp; Aug 12,2020</p>
<h3 class="abs post-title" style="left:822px;top:3666px;width:220px">Lorem ipsum dolor sitamet, consectetur adipiscing.</h3>
<p class="abs text-sm" style="left:822px;top:3718px;width:220px;font-size:9.5px;line-height:16px">Lorem ipsum dolor sit amet, consectetur adipiscing elit, sed deiusmod tempor incididunt ut labore et dolore.</p>

<div class="photo" role="img" aria-label="Photo of a presenter leading a meeting in a bright office" style="left:596px;top:3798px;width:204px;height:136px;background:linear-gradient(135deg,#f1f2f3,#c3c8cd 55%,#7e858e)"></div>
<p class="abs meta" style="left:822px;top:3798px">By : Admin &nbsp;&nbsp;|&nbsp;&nbsp; Aug 12,2020</p>
<h3 class="abs post-title" style="left:822px;top:3824px;width:220px">Lorem ipsum dolor sitamet, consectetur adipiscing.</h3>
<p class="abs text-sm" style="left:822px;top:3876px;width:220px;font-size:9.5px;line-height:16px">Lorem ipsum dolor sit amet, consectetur adipiscing elit, sed deiusmod tempor incididunt ut labore et dolore.</p>

<div class="photo" role="img" aria-label="Photo of an analyst reviewing charts on a monitor" style="left:596px;top:3956px;width:204px;height:136px;background:linear-gradient(135deg,#3c4150,#8d95a2 55%,#dfe2e6)"></div>
<p class="abs meta" style="left:822px;top:3956px">By : Admin &nbsp;&nbsp;|&nbsp;&nbsp; Aug 12,2020</p>
<h3 class="abs post-title" style="left:822px;top:3982px;width:220px">Lorem ipsum dolor sitamet, consectetur adipiscing.</h3>
<p class="abs text-sm" style="left:822px;top:4034px;width:220px;font-size:9.5px;line-height:16px">Lorem ipsum dolor sit amet, consectetur adipiscing elit, sed deiusmod tempor incididunt ut labore et dolore.</p>

<!-- ============ SOLUTIONS ============ -->
<div class="pink" style="left:0;top:4166px;width:1200px;height:574px"></div>
<h2 class="h2" style="left:162px;top:4226px">Tidewell Advisory<br><b>Solutions</b></h2>
<p class="abs text" style="left:162px;top:4310px;width:470px">Lorem ipsum dolor sit amet, consectetur adipiscing elieiusmod tempor incididunt ut labore et dolore magna aliqua.</p>
<div class="btn" style="left:822px;top:4232px;width:218px">Get Started With Us<span class="go"><svg width="14" height="14" viewBox="0 0 14 14"><path d="M3 11 L11 3 M5 3 H11 V9" stroke="#d7282f" stroke-width="2" fill="none"/></svg></span></div>
<div class="photo" role="img" aria-label="Photo of business partners shaking hands across a conference table" style="left:162px;top:4392px;width:878px;height:414px;background:linear-gradient(100deg,#4a3a32,#8b7d72 35%,#d8d4cf 60%,#6f7680)"></div>

<!-- ============ FOOTER ============ -->
<div class="brand" style="left:510px;top:4846px">
  <span class="brand-mark"></span>
  <span class="brand-name" style="font-size:20px;line-height:20px">TIDEWELL<br>ADVISORY</span>
</div>
<nav class="foot-links">
  <span>Home</span><span>|</span><span>About Us</span><span>|</span><span>The Team</span><span>|</span><span>What We do</span><span>|</span><span>Contact Us</span>
</nav>
<span class="social" role="img" aria-label="Social profile link" style="left:538px;top:4994px"></span>
<span class="social" role="img" aria-label="Social profile link" style="left:582px;top:4994px;background:#3b5a98"></span>
<span class="social" role="img" aria-label="Social profile link" style="left:626px;top:4994px;background:#1a76b3"></span>
<p class="copy">Copyright © TIDEWELL ADVISORY PTY LTD - 2020 - All Right Reserved</p>

</body>
</html>
```